Brightmoor Vector Systems Website

I am starting an IT consulting business called Brightmoor Vector Systems. I recently completed a logo contest on ArtHive and am now looking to put together a basic website. I can provide text and content but am looking for a site design with layout and graphics. I am attaching my logo below. I was thinking of a dark blue and white theme for the website (similar to the logo). However, I am open to ideas. Graphics can be a mix of business and high tech as that is the image I am trying to convey. The site will be relatively simple and probably have only 3 - 5 pages (Home, About Us, Services, Contact, etc.)
Target Market(s)
United States commercial companies and government contractors
Industry/Entity Type
Consulting

```html
<!DOCTYPE html>
<html lang="en">
<head>
<meta charset="utf-8">
<title>Brightmoor Vector Systems</title>
<link rel="stylesheet" href="https://fonts.googleapis.com/css2?family=Poppins:wght@300;400;500;600&family=Montserrat:wght@800&family=Barlow+Semi+Condensed:wght@600&display=swap">
<style>
:root{
  --navy:#0c3a6b;
  --navy-deep:#0d3366;
  --blue:#1a8fcd;
  --blue-bright:#14a0d8;
  --ink:#2b2b2b;
  --grey:#6b6b6b;
  --line:#c9d3de;
  --white:#ffffff;
}
*{box-sizing:border-box;margin:0;padding:0}
html,body{width:1200px;height:3112px;overflow:hidden;background:var(--white)}
body{position:relative;font-family:"Poppins",sans-serif;color:var(--ink)}
.abs{position:absolute}
.photo{position:absolute}
.shape{position:absolute;left:0;top:0}

/* header */
.brand{position:absolute;left:60px;top:12px;color:var(--white);display:flex;align-items:center;gap:10px}
.brand-dot{width:14px;height:14px;border-radius:50%;background:var(--blue-bright)}
.brand-name{font-family:"Poppins",sans-serif;font-weight:400;font-size:19px;letter-spacing:2px;line-height:1.1}
.nav{position:absolute;top:21px;left:586px;display:flex;gap:32px;font-size:13px;color:var(--white)}
.btn{position:absolute;display:flex;align-items:center;justify-content:space-between;padding-left:16px;padding-right:4px;border-radius:30px;background:var(--navy);color:var(--white);font-weight:500;font-size:14px;text-transform:uppercase}
.btn.light{background:var(--blue-bright)}
.btn-knob{width:32px;height:32px;border-radius:50%;background:var(--white);display:flex;align-items:center;justify-content:center}

/* hero */
.hero-title{position:absolute;left:60px;top:240px;font-family:"Montserrat",sans-serif;font-weight:800;font-size:56px;line-height:62px;color:var(--white);letter-spacing:1px}
.hero-text{position:absolute;left:62px;top:380px;width:460px;font-size:14.5px;line-height:21px;color:var(--white)}

/* headings */
.heading{position:absolute;font-family:"Barlow Semi Condensed",sans-serif;font-weight:600;font-size:31px;line-height:38px;color:var(--navy);text-transform:uppercase}
.heading span{color:var(--blue)}
.heading::before{content:"";position:absolute;left:-24px;top:2px;width:30px;height:30px;border-radius:50%;border:2px solid #dbe6ef}
.lead{position:absolute;font-size:13.5px;line-height:22.5px;color:var(--ink)}
.muted{position:absolute;font-size:12.5px;line-height:19.5px;color:var(--grey)}
.ticks{position:absolute;left:82px;top:834px;list-style:none}
.ticks li{display:flex;align-items:center;gap:16px;height:37.5px;font-size:13px;color:var(--grey)}
.tick{width:16px;height:16px;border-radius:50%;border:2px solid var(--blue);display:flex;align-items:center;justify-content:center}
.tick::after{content:"";width:6px;height:6px;border-radius:50%;background:var(--blue)}

/* services */
.services-title{position:absolute;left:0;width:1200px;top:1748px;text-align:center;font-size:31px;color:var(--white);font-weight:400;letter-spacing:1px}
.service{position:absolute;top:1870px;width:300px;text-align:center;color:var(--white)}
.service h3{font-weight:400;font-size:22px;margin-top:18px;letter-spacing:.5px}
.service p{font-size:12.5px;line-height:19.5px;margin-top:10px;font-weight:300}

/* form */
.field{position:absolute;border:1px solid var(--line);border-radius:20px;font-size:12px;color:var(--grey);padding-left:16px;display:flex;align-items:center}
.field.area{align-items:flex-start;padding-top:10px;border-radius:14px}

/* footer */
.footer{position:absolute;left:0;top:2812px;width:1200px;height:300px;background:var(--navy-deep);color:var(--white)}
.foot-brand{position:absolute;left:0;width:1200px;top:58px;text-align:center;font-size:28px;letter-spacing:3px;font-weight:400}
.foot-brand small{display:block;font-size:11px;letter-spacing:11px;margin-top:2px}
.foot-nav{position:absolute;left:0;width:1200px;top:130px;display:flex;justify-content:center;gap:18px;font-size:12.5px}
.foot-nav i{font-style:normal;opacity:.8}
.contact{position:absolute;top:170px;display:flex;gap:12px;font-size:12.5px;line-height:19px}
.contact-icon{width:34px;height:34px;border-radius:50%;background:var(--white);display:flex;align-items:center;justify-content:center;flex:none}
.social{position:absolute;top:230px;left:535px;display:flex;gap:6px}
.social span{width:28px;height:28px;border-radius:50%;border:1px solid var(--blue)}
.copy{position:absolute;left:62px;top:266px;font-size:12px}
</style>
</head>
<body>

<!-- hero -->
<svg class="shape" width="1200" height="720" aria-hidden="true">
  <defs>
    <linearGradient id="heroTone" x1="0" y1="0" x2="1" y2="1">
      <stop offset="0" stop-color="#2f6f9f"/>
      <stop offset=".5" stop-color="#5a93bd"/>
      <stop offset="1" stop-color="#7fb1d2"/>
    </linearGradient>
  </defs>
  <polygon points="0,0 1200,0 1200,652 877,660 520,652 0,628" fill="url(#heroTone)"/>
  <polygon points="877,659 1200,652 1200,713 877,690" fill="var(--blue)"/>
</svg>
<div class="photo" role="img" aria-label="Team meeting around a conference table led by a standing businesswoman" style="left:0;top:0;width:1200px;height:620px"></div>

<div class="brand"><span class="brand-dot"></span><span class="brand-name">BRIGHTMOOR VECTOR<br><small style="font-size:10px;letter-spacing:7px">SYSTEMS</small></span></div>
<nav class="nav"><span>Home</span><span>About Us</span><span>Services</span><span>Resources</span></nav>
<div class="btn light" style="left:927px;top:14px;width:209px;height:40px">Free Consultation<span class="btn-knob"><svg width="14" height="14" viewBox="0 0 14 14"><path d="M4 2l6 5-6 5" fill="none" stroke="#0c3a6b" stroke-width="2"/></svg></span></div>

<h1 class="hero-title">GROW YOUR<br>BUSSINESS</h1>
<p class="hero-text">Lorem Ipsum is simply dummy text of the printing and typesetting industry. Lorem Ipsum has been the industry's</p>
<div class="btn" style="left:60px;top:447px;width:154px;height:41px">Contact Us<span class="btn-knob"><svg width="14" height="14" viewBox="0 0 14 14"><path d="M4 2l6 5-6 5" fill="none" stroke="#0c3a6b" stroke-width="2"/></svg></span></div>

<!-- about -->
<div class="photo" role="img" aria-label="Two colleagues in business attire reviewing a folder together" style="left:517px;top:607px;width:360px;height:435px;background:linear-gradient(160deg,#d9dde2,#8d959c 60%,#3b3f44)"></div>
<div class="photo" role="img" aria-label="Smiling businesswoman holding a tablet in an office" style="left:915px;top:758px;width:225px;height:261px;background:linear-gradient(160deg,#e6ebef,#b9c2c9 55%,#2c2f33)"></div>

<h2 class="heading" style="left:85px;top:697px">About <span>Us</span></h2>
<p class="lead" style="left:84px;top:750px;width:350px">Lorem Ipsum is simply dummy text of the printing and typesetting industry. Lorem Ipsum has been the industry's</p>
<ul class="ticks">
  <li><span class="tick"></span>It is a long established fact</li>
  <li><span class="tick"></span>There are many variations of passages</li>
  <li><span class="tick"></span>sure there isn't anything embarrassing</li>
  <li><span class="tick"></span>cites of the word in classical literature</li>
</ul>
<div class="btn" style="left:82px;top:999px;width:157px;height:40px">Learn More<span class="btn-knob"><svg width="14" height="14" viewBox="0 0 14 14"><path d="M4 2l6 5-6 5" fill="none" stroke="#0c3a6b" stroke-width="2"/></svg></span></div>

<!-- consulting -->
<div class="photo" role="img" aria-label="Smiling young man with glasses working on a laptop" style="left:85px;top:1118px;width:586px;height:562px;background:radial-gradient(ellipse at 45% 55%,#c9dbe8 0%,#e9f0f5 55%,#ffffff 75%)"></div>
<h2 class="heading" style="left:718px;top:1228px;width:400px">Get your IT consulting<br>business <span>right up<br>there</span></h2>
<p class="muted" style="left:718px;top:1355px;width:372px">There are many variations of passages of Lorem Ipsum available, but the majority have suffered alteration in some form, by injected humour, or randomised words which don't look even slightly believable. If you are going to use a passage of Lorem Ipsum, you need to be sure</p>
<div class="btn" style="left:715px;top:1478px;width:218px;height:40px">Request a call back<span class="btn-knob"><svg width="14" height="14" viewBox="0 0 14 14"><path d="M4 2l6 5-6 5" fill="none" stroke="#0c3a6b" stroke-width="2"/></svg></span></div>

<!-- services -->
<svg class="shape" style="top:1630px" width="1200" height="600" aria-hidden="true">
  <defs>
    <linearGradient id="svcTone" x1="0" y1="0" x2="1" y2="1">
      <stop offset="0" stop-color="#1f8fcb"/>
      <stop offset=".5" stop-color="#3aa3d8"/>
      <stop offset="1" stop-color="#1b90cc"/>
    </linearGradient>
  </defs>
  <polygon points="0,34 1200,7 1200,533 0,581" fill="url(#svcTone)"/>
  <polygon points="0,34 560,52 0,92" fill="var(--navy)"/>
</svg>
<div class="photo" role="img" aria-label="Office team collaborating, tinted in blue" style="left:0;top:1660px;width:1200px;height:520px"></div>
<h2 class="services-title">OUR SERVICES</h2>

<div class="service" style="left:75px">
  <svg width="112" height="112" viewBox="0 0 112 112" aria-hidden="true"><circle cx="56" cy="56" r="48" fill="none" stroke="#0c3a6b" stroke-width="8" stroke-dasharray="230 72"/><path d="M36 74h40M40 72V60M48 72V52M56 72V56M64 72V46M38 56l12-10 8 6 16-14" fill="none" stroke="#fff" stroke-width="2.5"/></svg>
  <h3>Strategic Planning</h3>
  <p>Contrary to popular belief, Lorem Ipsum is not simply random text. It has roots in a piece of classical</p>
</div>
<div class="service" style="left:457px">
  <svg width="112" height="112" viewBox="0 0 112 112" aria-hidden="true"><circle cx="56" cy="56" r="48" fill="none" stroke="#0c3a6b" stroke-width="8" stroke-dasharray="230 72"/><path d="M34 44h44M38 44v-8l18-8 18 8v8M34 66l10-8 12 10 12-10 10 8" fill="none" stroke="#fff" stroke-width="2.5"/></svg>
  <h3>Acquisition Support</h3>
  <p>Contrary to popular belief, Lorem Ipsum is not simply random text. It has roots in a piece of classical</p>
</div>
<div class="service" style="left:847px">
  <svg width="112" height="112" viewBox="0 0 112 112" aria-hidden="true"><circle cx="56" cy="56" r="48" fill="none" stroke="#0c3a6b" stroke-width="8" stroke-dasharray="230 72"/><rect x="38" y="40" width="36" height="30" fill="none" stroke="#fff" stroke-width="2.5"/><circle cx="56" cy="55" r="7" fill="none" stroke="#fff" stroke-width="2.5"/><path d="M44 40v-8M56 40v-10M68 40v-8" stroke="#fff" stroke-width="2.5"/></svg>
  <h3>Program Management</h3>
  <p>Contrary to popular belief, Lorem Ipsum is not simply random text. It has roots in a piece of classical</p>
</div>

<!-- contact -->
<svg class="shape" style="top:2230px" width="1200" height="60" aria-hidden="true"><polygon points="1140,5 1200,0 1200,48 1140,52" fill="var(--blue)"/></svg>
<div class="photo" role="img" aria-label="Two businessmen shaking hands and smiling" style="left:727px;top:2205px;width:413px;height:524px;background:linear-gradient(160deg,#8fa6b6,#5d6e7b 55%,#2d3640)"></div>

<h2 class="heading" style="left:85px;top:2312px">Get in <span>Touch</span></h2>
<p class="muted" style="left:84px;top:2364px;width:300px">We work with ambitious leaders who want to define the future, not hide from it.</p>
<div class="field" style="left:82px;top:2425px;width:262px;height:37px">Name :</div>
<div class="field" style="left:360px;top:2425px;width:262px;height:37px">Email :</div>
<div class="field" style="left:82px;top:2477px;width:262px;height:38px">Phone :</div>
<div class="field" style="left:360px;top:2477px;width:262px;height:38px">Company Name :</div>
<div class="field area" style="left:82px;top:2530px;width:540px;height:89px">Message :</div>
<div class="btn" style="left:82px;top:2644px;width:157px;height:40px">Submit Now<span class="btn-knob"><svg width="14" height="14" viewBox="0 0 14 14"><path d="M4 2l6 5-6 5" fill="none" stroke="#0c3a6b" stroke-width="2"/></svg></span></div>

<!-- footer -->
<footer class="footer">
  <div class="foot-brand">BRIGHTMOOR VECTOR<small>SYSTEMS</small></div>
  <nav class="foot-nav"><span>Home</span><i>|</i><span>About us</span><i>|</i><span>Services</span><i>|</i><span>Resources</span><i>|</i><span>Contact Us</span></nav>
  <div class="contact" style="left:278px"><span class="contact-icon"><svg width="14" height="18" viewBox="0 0 14 18"><path d="M7 1a6 6 0 0 0-6 6c0 4.5 6 10 6 10s6-5.5 6-10a6 6 0 0 0-6-6z" fill="#1a8fcd"/><circle cx="7" cy="7" r="2.2" fill="#fff"/></svg></span><span>101- Lorem Ipsum is dummy<br>printing text</span></div>
  <div class="contact" style="left:548px"><span class="contact-icon"><svg width="16" height="12" viewBox="0 0 16 12"><rect x="0.5" y="0.5" width="15" height="11" fill="#1a8fcd"/><path d="M1 1l7 6 7-6" fill="none" stroke="#fff" stroke-width="1.4"/></svg></span><span>info@brightmoorvector.com</span></div>
  <div class="contact" style="left:795px"><span class="contact-icon"><svg width="16" height="16" viewBox="0 0 16 16"><path d="M3 1l3 3-2 2c1 2 3 4 5 5l2-2 3 3-2 3C7 15 1 9 1 3z" fill="#1a8fcd"/></svg></span><span style="padding-top:7px">123 456 7890</span></div>
  <div class="abs" style="left:0;top:244px;width:1200px;height:1px;background:rgba(26,143,205,.5)"></div>
  <div class="social"><span style="background:var(--navy-deep)"></span><span style="background:var(--navy-deep)"></span><span style="background:var(--navy-deep)"></span><span style="background:var(--navy-deep)"></span></div>
  <p class="copy">©BRIGHTMOOR VECTOR - 2021 .All Right Reserved</p>
</footer>

</body>
</html>
```